Bright and beautiful business card for a coach

I'm a personal and business coach based in Perth, Australia. I need a business card that whilst subtle and elegant, will stand out and appeal on a table full of cards.

My business name is Tide Mentoring and the business card must represent the warmth and brightness implied in the name, without being gimmicky. It must have a warmth and appeal and be easy to read.

I prefer clean, minimalist designs.

It must align with the feel of my website and socials: https://www.tidementoring.com.au/
https://www.instagram.com/tidementoringau/
https://www.facebook.com/tidementoringau
Updates

Hi Designers Thank you so much for taking the time to submit designs. I wonder if I could have explained myself a little better. Most of the designs that have been submitted look rather formal and many have quite corporate looking embellishments on them (to my eye). I would like softer, warmer, more organic. I’m open to people playing about and being more abstract, using softer embellishments (e.g the line drawing flowers and grasses I’ve used in my socials) incorporating other colours from my palette or like the social icons in my email signature (in PDF), perhaps playing with size/oversize, playing with the bleed. Please don’t be constrained by what I’ve already done, it merely needs to compliment. I’m sorry if I’m not using the right words or have led you astray. I’m no designer, but I’ve done my website, socials, email signature etc all myself (my logo was a design contest) and I was really hoping for my business card to be something more creative than I could have made with a template. Reminder: No black cards/sides please. Thank you 😊

Target Market(s)

Individuals, most likely but not all female. Creative thinkers. Likely professionals.

Industry/Entity Type

Business & Personal Coach

Contact Information for Business Card

(Tide Mentoring Logo) Name: Maren Delsby; Title: Business & Personal Coach; Phone number: +61 (0)438 915307; Email: maren@tidementoring.com.au; Website: https://tidementoring.com.au; Social icons for Facebook, Instagram & LinkedIn: @tidementoringAU. Optional strapline: "A thinking partner to help you cut through the noise"

Font styles to use
Sans Serif

Colors
00AB8E
00BBA5
67D7C9
C6EFE9
E9F9F6
59FF00
82FF00
B8FF75
E3FFCB
F4FFEA
FFC000
F8CF3A
FAE287
FDF2CF
FEFAEE

Requirements
Must have
• Must align with feel of my website and socials. Must have a pop of #FFC000 (possibly whole of one side, or at least a block). Bright or white background. Easy to read.
Nice to have
• Possibly incorporate the sunshine/grass picture I have used in website and socials - will upload.
Should not have
• Must not be black or dark. Not impersonal or corporate looking.

```html
<!DOCTYPE html>
<html lang="en">
<head>
<meta charset="utf-8">
<title>Tide Mentoring – Business Card</title>
<link rel="stylesheet" href="https://fonts.googleapis.com/css2?family=Montserrat:wght@500;600;700&display=swap">
<style>
  :root {
    --page: #ffffff;
    --card: #fefaee;
    --gold: #d4882a;
    --sun: #ffc000;
    --grey: #62676e;
    --pill-grey: #a3a6aa;
    --shade: rgba(0, 0, 0, 0.18);
  }
  * { margin: 0; padding: 0; box-sizing: border-box; }
  html, body {
    width: 1200px; height: 1200px; overflow: hidden;
    background: var(--page);
    font-family: "Montserrat", sans-serif;
  }
  .card {
    position: absolute; left: 286px; width: 630px; height: 360px;
    background: var(--card);
    box-shadow: 0 2px 8px var(--shade);
    overflow: hidden;
  }
  .card--front { top: 186px; }
  .card--back { top: 639px; }

  .foliage {
    position: absolute;
    background: radial-gradient(ellipse at center, rgba(255, 192, 0, 0.22) 0%, rgba(254, 250, 238, 0) 70%);
  }
  .card--front .foliage { left: 330px; top: 270px; width: 300px; height: 100px; }
  .card--back .foliage { left: 0; top: -20px; width: 630px; height: 130px; }

  .brand {
    position: absolute; color: var(--gold);
    font-weight: 600; white-space: nowrap; text-align: center;
  }
  .card--front .brand { left: 37px; top: 137px; width: 233px; font-size: 29px; }
  .card--back .brand { left: 0; top: 150px; width: 630px; font-size: 36px; }

  .socials { position: absolute; left: 104px; top: 244px; display: flex; gap: 15px; }
  .socials span {
    width: 28px; height: 28px; border-radius: 50%; background: var(--gold); display: block;
  }

  .divider {
    position: absolute; left: 305px; top: 87px; width: 1px; height: 183px;
    background: linear-gradient(to bottom, rgba(212,136,42,0), rgba(212,136,42,0.6) 50%, rgba(212,136,42,0));
  }

  .contact { position: absolute; right: 42px; top: 97px; text-align: right; }
  .contact__name { color: var(--gold); font-weight: 700; font-size: 27px; letter-spacing: 0.5px; line-height: 1; }
  .contact__title { color: var(--grey); font-weight: 600; font-size: 14.8px; margin-top: 10px; letter-spacing: 0.2px; }
  .contact__rule { width: 83px; height: 2px; background: var(--gold); margin: 10px 0 0 auto; }
  .contact__phone { color: var(--grey); font-weight: 600; font-size: 17.8px; margin-top: 20px; letter-spacing: 0.3px; }
  .contact__email { color: var(--grey); font-weight: 500; font-size: 13.8px; margin-top: 5px; }
  .contact__email b { color: var(--gold); font-weight: 600; }

  .web-pill {
    position: absolute; left: 389px; top: 239px; width: 203px; height: 25px;
    background: var(--gold); border-radius: 5px;
    color: #fff; font-weight: 600; font-size: 13.5px; line-height: 25px;
    padding-left: 38px;
  }
  .web-pill__icon {
    position: absolute; left: 0; top: 0; width: 31px; height: 25px;
    background: var(--pill-grey); border-radius: 5px 12px 12px 5px;
    display: flex; align-items: center; justify-content: center;
  }

  .card--back .url {
    position: absolute; left: 0; top: 257px; width: 630px; text-align: center;
    color: var(--gold); font-weight: 600; font-size: 18.8px; letter-spacing: 0.3px;
  }
</style>
</head>
<body>
  <section class="card card--front">
    <div class="foliage" role="img" aria-label="Faint sunlit grass silhouette"></div>
    <div class="brand">Tide Mentoring</div>
    <div class="socials" aria-label="Social links">
      <span></span><span></span><span></span>
    </div>
    <div class="divider"></div>
    <div class="contact">
      <div class="contact__name">MAREN DELSBY</div>
      <div class="contact__title">BUSINESS &amp; PERSONAL COACH</div>
      <div class="contact__rule"></div>
      <div class="contact__phone">+61 (0)438 915307</div>
      <div class="contact__email"><b>Email:</b> maren@tidementoring.com.au</div>
    </div>
    <div class="web-pill">
      <span class="web-pill__icon">
        <svg width="17" height="17" viewBox="0 0 20 20" fill="none" stroke="#fff" stroke-width="1.3">
          <circle cx="10" cy="10" r="8"/>
          <ellipse cx="10" cy="10" rx="3.5" ry="8"/>
          <line x1="2" y1="10" x2="18" y2="10"/>
          <path d="M3.5 5.5h13M3.5 14.5h13"/>
        </svg>
      </span>
      tidementoring.com.au
    </div>
  </section>

  <section class="card card--back">
    <div class="foliage" role="img" aria-label="Faint sunlit grass silhouette"></div>
    <div class="brand">Tide Mentoring</div>
    <div class="url">www.tidementoring.com.au</div>
  </section>
</body>
</html>
```